Qualvine.com needs a Mobile FIRST Site

Qualvine.com is an insurance broker based in Panama City, Panama that plans to sell car and motorcycle insurance online.

We need to design a total of 5 pages (two of those are A/B test pages). The site will be responsive and will be programmed in React. We will be using Bolt Kit´s library to code Qualvine.com. Keep in mind that we are using Bolt Kit to program the site´s functions, not to create the "look and feel" of the site, that is obviously your job. You can learn more about Bolt Kit here... https://boltkit.example/

We have created wireframes for the app. Please follow and keep in mind the instructions in the wireframes. You can change things here and there as long as the core functions and goals stay intact. We have uploaded the wireframes along with the company logo and color.

We are planning to A/B test the site´s home page so we need to design two homepages. You can find homepage A and B in the wireframes provided.

We speak Spanish in Panama but you can design the site in English. We can change the text once we receive the designs.

Target Market(s)

25-45 year olds who own a car or motorcylcle and own a credit card.

Industry/Entity Type

Insurance

Font styles to use
Sans Serif

Requirements
Must have
• Follow the wireframes provided and the logo colors.
Nice to have
• Please look at the Image I´ve uploaded from DeskHarbor, use it as reference to create HomePage A.

```html
<!DOCTYPE html>
<html lang="es">
<head>
<meta charset="utf-8">
<title>Qualvine.com – Elige tu seguro</title>
<link rel="stylesheet" href="https://fonts.googleapis.com/css2?family=Montserrat:wght@400;500;600;700&display=swap">
<style>
  :root{
    --purple:#472c87;
    --purple-bright:#6a3ee6;
    --purple-deep:#3b1f86;
    --ink:#4a4a4a;
    --muted:#9a9a9a;
    --soft-bg:#f5f5f5;
    --rule:#e4e4e4;
    --bar-track:#a9a8ad;
    --white:#ffffff;
  }
  *{box-sizing:border-box;margin:0;padding:0}
  html,body{width:838px;height:1200px;overflow:hidden;background:var(--white)}
  body{font-family:'Montserrat',sans-serif;color:var(--ink)}
  .site-header{height:160px;background:var(--purple);display:flex;align-items:center;justify-content:center}
  .brand-name{color:var(--white);font-size:50px;font-weight:700;letter-spacing:-1px}
  .intro{background:var(--soft-bg);height:218px;padding-top:34px;text-align:center}
  .intro-text{font-size:19px;color:#6b6b6b}
  .stepper{position:relative;width:838px;height:140px;margin-top:26px}
  .step-line{position:absolute;top:33px;height:3px;background:#bdbdbd}
  .step-line.done{background:var(--purple)}
  .step{position:absolute;top:0;width:120px;margin-left:-60px;text-align:center}
  .step-dot{width:68px;height:68px;border-radius:50%;margin:0 auto;border:3px solid #c9c9c9;background:var(--white);
    display:flex;align-items:center;justify-content:center;font-size:28px;color:#9a9a9a;font-weight:500}
  .step.active .step-dot{background:var(--purple);border-color:var(--purple);color:var(--white)}
  .step-label{margin-top:8px;font-size:20px;font-weight:600;color:#a5a5a5}
  .step.active .step-label{color:var(--purple)}
  .tabs{display:flex;height:84px;border-bottom:3px solid #d6d6d6;position:relative}
  .tab{flex:1;display:flex;align-items:center;justify-content:center;gap:18px;font-size:29px;font-weight:600;color:#a5a5a5}
  .tab.active{color:var(--purple);border-bottom:4px solid var(--purple-bright);margin-bottom:-3px}
  .plan{position:relative;height:367px;border-bottom:5px solid var(--rule)}
  .plan:last-child{border-bottom:none}
  .plan-photo{position:absolute;left:82px;top:34px;width:210px;height:200px;border-radius:50%;
    background:radial-gradient(ellipse at 50% 55%,#3a3a40 0%,#1e1e24 45%,#8c8c92 75%,#ffffff 100%)}
  .plan-price{position:absolute;left:0;width:374px;top:258px;text-align:center;color:var(--purple-deep);font-weight:600;font-size:40px}
  .plan-price small{font-size:26px;font-weight:700;margin-right:6px}
  .buy-btn{position:absolute;left:68px;top:315px;width:246px;height:48px;border-radius:10px;background:var(--purple);
    color:var(--white);font-weight:700;font-size:21px;letter-spacing:1px;display:flex;align-items:center;justify-content:center;
    box-shadow:0 6px 10px rgba(0,0,0,.25)}
  .limits{position:absolute;left:391px;top:36px;width:385px}
  .limit-label{font-size:19px;font-weight:500;color:#555;margin-bottom:6px}
  .bar{height:24px;border-radius:4px;background:var(--bar-track);margin-bottom:24px;position:relative}
  .bar-fill{height:100%;border-radius:4px;background:linear-gradient(90deg,var(--purple-bright),var(--purple-deep));
    color:var(--white);font-size:16px;font-weight:700;display:flex;align-items:center;justify-content:flex-end;padding-right:10px}
  .benefits{position:absolute;left:391px;top:212px;width:420px}
  .benefits-title{font-size:24px;font-weight:600;color:var(--purple-deep)}
  .benefit-list{display:flex;margin-top:16px}
  .benefit{width:155px;text-align:center;margin-left:-40px}
  .benefit:first-child{margin-left:-30px}
  .benefit svg{display:block;margin:0 auto 10px}
  .benefit-text{font-size:15px;color:#8b8b8b}
</style>
</head>
<body>
  <header class="site-header">
    <span class="brand-name">Qualvine.com</span>
  </header>

  <section class="intro">
    <p class="intro-text">Sample text goes here to fill blank areas.&nbsp; Sample text</p>
    <div class="stepper">
      <div class="step-line done" style="left:229px;width:157px"></div>
      <div class="step-line" style="left:454px;width:157px"></div>
      <div class="step active" style="left:195px"><div class="step-dot">1</div><div class="step-label">Elige</div></div>
      <div class="step" style="left:420px"><div class="step-dot">2</div><div class="step-label">Datos</div></div>
      <div class="step" style="left:645px"><div class="step-dot">3</div><div class="step-label">Pago</div></div>
    </div>
  </section>

  <nav class="tabs">
    <div class="tab">
      <svg width="44" height="34" viewBox="0 0 44 34" fill="none" stroke="#a5a5a5" stroke-width="2.5" stroke-linejoin="round">
        <path d="M8 14 L12 4 H32 L36 14"/><rect x="3" y="14" width="38" height="12" rx="3"/>
        <path d="M8 26v5h6v-5M30 26v5h6v-5"/><circle cx="10" cy="20" r="2"/><circle cx="34" cy="20" r="2"/>
      </svg>
      Carros
    </div>
    <div class="tab active">
      <svg width="52" height="32" viewBox="0 0 52 32" fill="none" stroke="var(--purple)" stroke-width="2.5" stroke-linejoin="round" stroke-linecap="round">
        <circle cx="10" cy="22" r="8"/><circle cx="42" cy="22" r="8"/>
        <path d="M10 22 L20 12 H30 L36 8 M30 12 L42 22 M20 12 L24 20 H32 M14 8 H22"/>
      </svg>
      Motos
    </div>
  </nav>

  <main>
    <article class="plan">
      <div class="plan-photo" role="img" aria-label="Foto de una motocicleta deportiva negra"></div>
      <div class="plan-price"><small>$</small>150</div>
      <div class="buy-btn">COMPRAR</div>
      <div class="limits">
        <div class="limit-label">Límite por Accidente</div>
        <div class="bar"><div class="bar-fill" style="width:62%">$ 10,000</div></div>
        <div class="limit-label">Límite por Año</div>
        <div class="bar"><div class="bar-fill" style="width:71%">$ 15,000</div></div>
      </div>
      <div class="benefits">
        <div class="benefits-title">Beneficios</div>
        <div class="benefit-list">
          <div class="benefit"><svg width="44" height="44" viewBox="0 0 44 44" fill="none" stroke="var(--purple-deep)" stroke-width="3" stroke-linecap="round" stroke-linejoin="round"><circle cx="22" cy="22" r="19"/><path d="M13 22l6 6 12-12"/></svg><div class="benefit-text">Sample text</div></div>
          <div class="benefit"><svg width="44" height="44" viewBox="0 0 44 44" fill="none" stroke="var(--purple-deep)" stroke-width="3" stroke-linecap="round" stroke-linejoin="round"><circle cx="22" cy="22" r="19"/><path d="M22 11v12h9"/></svg><div class="benefit-text">Sample text</div></div>
          <div class="benefit"><svg width="44" height="44" viewBox="0 0 44 44" fill="none" stroke="var(--purple-deep)" stroke-width="3" stroke-linecap="round"><circle cx="22" cy="22" r="19"/><path d="M15 29l14-14"/><circle cx="16" cy="16" r="2"/><circle cx="28" cy="28" r="2"/></svg><div class="benefit-text">Sample text</div></div>
        </div>
      </div>
    </article>

    <article class="plan">
      <div class="plan-photo" role="img" aria-label="Foto de una motocicleta deportiva negra"></div>
      <div class="plan-price"><small>$</small>150</div>
      <div class="buy-btn">COMPRAR</div>
      <div class="limits">
        <div class="limit-label">Límite por Accidente</div>
        <div class="bar"><div class="bar-fill" style="width:62%">$ 10,000</div></div>
        <div class="limit-label">Límite por Año</div>
        <div class="bar"><div class="bar-fill" style="width:71%">$ 15,000</div></div>
      </div>
      <div class="benefits">
        <div class="benefits-title">Beneficios</div>
        <div class="benefit-list">
          <div class="benefit"><svg width="44" height="44" viewBox="0 0 44 44" fill="none" stroke="var(--purple-deep)" stroke-width="3" stroke-linecap="round" stroke-linejoin="round"><circle cx="22" cy="22" r="19"/><path d="M13 22l6 6 12-12"/></svg><div class="benefit-text">Sample text</div></div>
          <div class="benefit"><svg width="44" height="44" viewBox="0 0 44 44" fill="none" stroke="var(--purple-deep)" stroke-width="3" stroke-linecap="round" stroke-linejoin="round"><circle cx="22" cy="22" r="19"/><path d="M22 11v12h9"/></svg><div class="benefit-text">Sample text</div></div>
          <div class="benefit"><svg width="44" height="44" viewBox="0 0 44 44" fill="none" stroke="var(--purple-deep)" stroke-width="3" stroke-linecap="round"><circle cx="22" cy="22" r="19"/><path d="M15 29l14-14"/><circle cx="16" cy="16" r="2"/><circle cx="28" cy="28" r="2"/></svg><div class="benefit-text">Sample text</div></div>
        </div>
      </div>
    </article>
  </main>
</body>
</html>
```